依頼詳細
ゴミ屋敷の片づけ・遺品整理等の事業になります。
ポスティングを想定しています。
ターゲットは高齢者になりますのでわかりやすいデザインでお願いします。
記載項目
屋号:そよかぜクリーンサービス
電話番号:未定
サイズ
A4
ページ数
両面
希望イメージ
シンプル 複雑
単色 カラフル
暗い 明るい
日常 高級
遊び心 厳粛
未来的 伝統的
女性的 男性的
希望する色
緑系
納品ファイル
• 高解像度JPG (.jpg)
補足説明
■ 選んだ理由

高齢者向けということでイラストを多用しわかりやすいデザインで気に入りました。
ベースもやさしめの色合いで好きです。

■ 提案者全員のお礼・コメント

さまざまな提案をいただき感謝しています。ありがとうございました。

```html
<!DOCTYPE html>
<html lang="ja">
<head>
<meta charset="utf-8">
<title>そよかぜクリーンサービス チラシ</title>
<link href="https://fonts.googleapis.com/css2?family=M+PLUS+Rounded+1c:wght@500;700;800&family=Noto+Sans+JP:wght@400;500;700;900&display=swap" rel="stylesheet">
<style>
:root{
  --green:#3fa535;
  --green-dark:#23862a;
  --green-light:#e6f3d8;
  --green-pale:#f2f8ea;
  --orange:#ef7d14;
  --red:#e33a1c;
  --ink:#333;
  --white:#fff;
  --line:#b9d9a6;
}
*{box-sizing:border-box;margin:0;padding:0}
html,body{width:846px;height:1200px;overflow:hidden;background:var(--white)}
body{font-family:"Noto Sans JP",sans-serif;color:var(--ink);position:relative}
.flyer{width:846px;height:1200px;position:relative;overflow:hidden}
.headline{font-family:"M PLUS Rounded 1c",sans-serif;font-weight:800;color:var(--green);font-size:29px;text-align:center;padding-top:14px;white-space:nowrap;line-height:1.3}
.subline{margin:8px 22px 0;background:var(--green-pale);text-align:center;color:var(--orange);font-family:"M PLUS Rounded 1c",sans-serif;font-weight:800;font-size:26px;padding:3px 0;border-radius:4px;white-space:nowrap}
.subline small{font-size:21px;margin-right:14px}
.packs{display:flex;gap:14px;margin:12px 22px 0}
.pack{flex:1;border:3px solid var(--green);border-radius:8px;height:166px;position:relative;background:var(--white);overflow:hidden}
.pack-title{font-family:"M PLUS Rounded 1c",sans-serif;font-weight:800;color:var(--green-dark);font-size:19px;position:absolute;left:84px;top:10px;line-height:1.2;white-space:nowrap;letter-spacing:-.5px}
.pack-title.long{font-size:16px;top:12px}
.pack-note{position:absolute;left:86px;top:40px;font-size:12px;color:var(--ink);line-height:1.5;white-space:nowrap}
.pack-art{position:absolute;left:8px;top:10px;width:70px;height:68px;border-radius:6px;background:linear-gradient(#6cc05f,#3fa535)}
.pack-price{position:absolute;left:0;right:0;bottom:0;background:var(--green-light);height:66px;display:flex;align-items:center;justify-content:center;font-family:"M PLUS Rounded 1c",sans-serif;font-weight:800;font-size:36px;color:var(--green-dark)}
.pack-price span{font-size:21px}
.notes{margin:10px 22px 0;font-size:11.5px;line-height:1.6;color:var(--ink)}
.buy{margin:6px 22px 0;display:flex;align-items:center;gap:8px;font-weight:900;color:var(--orange);font-size:17px}
.buy i{display:inline-block;width:20px;height:20px;border-radius:50%;background:var(--orange)}
.recycle{margin:5px 22px 0;font-size:11.5px;display:flex;gap:10px;align-items:center}
.recycle b{background:var(--green);color:var(--white);padding:2px 8px;border-radius:3px;font-size:12px;white-space:nowrap}
.section-label{margin:8px 22px 4px;font-weight:900;color:var(--green-dark);font-size:15px}
.fees{margin:0 22px;display:flex;gap:14px}
.fees table{flex:1;border-collapse:collapse;font-size:14px}
.fees td{border-bottom:1px dashed var(--line);padding:3px 8px;height:27px}
.fees tr:nth-child(odd) td{background:var(--green-pale)}
.fees td.price{text-align:right;font-weight:700}
.options{margin:8px 22px 0;border:2px solid var(--green);border-radius:6px;padding:5px 12px 6px;font-size:12px;line-height:1.65}
.options h3{display:inline-block;background:var(--green);color:var(--white);font-size:12px;padding:1px 10px;border-radius:3px;margin-bottom:2px}
.bottom{position:absolute;left:0;top:768px;width:846px;height:432px;background:var(--green)}
.lady{position:absolute;left:18px;top:14px;width:120px;height:140px;border-radius:10px;background:linear-gradient(#bde3a8,#8fcf76)}
.features{position:absolute;left:150px;top:12px;display:flex;gap:10px}
.feature{width:104px;height:104px;border-radius:50%;background:var(--white);display:flex;flex-direction:column;align-items:center;justify-content:center;font-weight:900;color:var(--green-dark);font-size:15px;text-align:center;line-height:1.3}
.feature svg{margin-bottom:4px}
.budget{position:absolute;left:150px;top:124px;width:676px;height:40px;background:var(--white);border-radius:20px;display:flex;align-items:center;justify-content:center;font-family:"M PLUS Rounded 1c",sans-serif;font-weight:800;color:var(--red);font-size:23px;white-space:nowrap}
.flow{position:absolute;left:18px;top:178px;right:18px;height:90px;display:flex;align-items:center;gap:6px}
.flow-label{width:70px;height:86px;background:var(--green-dark);color:var(--white);font-weight:900;font-size:17px;display:flex;align-items:center;justify-content:center;text-align:center;line-height:1.3;border-radius:6px}
.step{flex:1;height:86px;background:var(--white);border-radius:6px;display:flex;align-items:center;justify-content:center;font-weight:900;font-size:17px;color:var(--green-dark);white-space:nowrap}
.arrow{width:0;height:0;border-top:12px solid transparent;border-bottom:12px solid transparent;border-left:14px solid var(--white)}
.contact{position:absolute;left:18px;right:18px;top:286px;height:128px;background:var(--white);border-radius:10px;display:flex;align-items:center;padding:0 20px;gap:16px}
.contact p{font-weight:900;color:var(--green-dark);font-size:16px;line-height:1.6;width:250px;flex:none}
.contact p strong{color:var(--red)}
.tel{font-family:"M PLUS Rounded 1c",sans-serif;font-weight:800;font-size:54px;color:var(--green-dark);white-space:nowrap;display:flex;align-items:center;gap:4px}
.tel span{font-size:34px}
</style>
</head>
<body>
<main class="flyer">
  <h1 class="headline">お部屋の片づけ・ゴミ屋敷整理・遺品整理・不用品回収</h1>
  <p class="subline"><small>お得なパック料金</small>まとめてお得!パック料金をご用意!</p>

  <section class="packs">
    <div class="pack">
      <div class="pack-art" role="img" aria-label="軽トラックのイラスト"></div>
      <div class="pack-title">軽トラック1台分</div>
      <div class="pack-note">(単身〜1K程度量)<br>荷台容量約2㎥</div>
      <div class="pack-price">20,000<span>円〜</span></div>
    </div>
    <div class="pack">
      <div class="pack-art" role="img" aria-label="2tトラックのイラスト"></div>
      <div class="pack-title">2tトラック1台分</div>
      <div class="pack-note">(1K〜1DK程度)<br>荷台容量約4㎥</div>
      <div class="pack-price">45,000<span>円〜</span></div>
    </div>
    <div class="pack">
      <div class="pack-art" role="img" aria-label="2t箱型トラックのイラスト"></div>
      <div class="pack-title long">2t箱型トラック1台分</div>
      <div class="pack-note">(2DK〜2LDK程度)<br>荷台容量約8㎥</div>
      <div class="pack-price">85,000<span>円</span></div>
    </div>
  </section>

  <p class="notes">●料金は作業員の人件費・車両費・処分費を含みます。階段作業や大型家具の解体が必要な場合は別途料金がかかることがあります。●家電リサイクル品は別料金となります。●事前にお見積りをお出しし、ご納得いただいてから作業いたしますのでご安心ください。</p>

  <div class="buy"><i></i>買取可能なお品物はその場で買取!</div>
  <div class="recycle"><b>リサイクル&amp;リユース</b>家具・家電・骨董品などまだ使える品物は査定のうえ買取し、回収料金から差し引きます。</div>

  <h2 class="section-label">不用品回収料金表</h2>
  <div class="fees">
    <table>
      <tr><td>木製チェア</td><td class="price">2300円</td></tr>
      <tr><td>テレビ台(20インチまで)</td><td class="price">1950円</td></tr>
      <tr><td>カラーボックス2段</td><td class="price">1560円</td></tr>
      <tr><td>スチールシェルフ(小)</td><td class="price">910円</td></tr>
      <tr><td>食器棚(60センチ幅)</td><td class="price">5500円</td></tr>
      <tr><td>レンジ台</td><td class="price">2100円</td></tr>
      <tr><td>整理収納棚</td><td class="price">2100円</td></tr>
    </table>
    <table>
      <tr><td>木製チェア</td><td class="price">2300円</td></tr>
      <tr><td>テレビ台(20インチまで)</td><td class="price">1950円</td></tr>
      <tr><td>カラーボックス2段</td><td class="price">1560円</td></tr>
      <tr><td>スチールシェルフ(小)</td><td class="price">910円</td></tr>
      <tr><td>食器棚(60センチ幅)</td><td class="price">5500円</td></tr>
      <tr><td>レンジ台</td><td class="price">2100円</td></tr>
      <tr><td>整理収納棚</td><td class="price">2100円</td></tr>
    </table>
  </div>

  <div class="options">
    <h3>オプション料金</h3><br>
    ●階段作業(2階以上)1階につき 500円〜 ●家具の解体 1,000円〜 ●エアコン取外し 5,000円〜<br>
    ●ハウスクリーニング 1部屋 8,000円〜 ●消臭・除菌作業 4,000円〜 その他お気軽にご相談ください
  </div>

  <section class="bottom">
    <div class="lady" role="img" aria-label="笑顔で案内するスタッフのイラスト"></div>
    <div class="features">
      <div class="feature"><svg width="28" height="22" viewBox="0 0 28 22"><rect x="2" y="2" width="24" height="18" rx="2" fill="none" stroke="#3fa535" stroke-width="3"/><path d="M7 11l5 5 9-10" fill="none" stroke="#3fa535" stroke-width="3"/></svg>見積無料</div>
      <div class="feature"><svg width="24" height="24" viewBox="0 0 24 24"><rect x="3" y="10" width="18" height="12" rx="2" fill="#3fa535"/><path d="M7 10V7a5 5 0 0110 0v3" fill="none" stroke="#3fa535" stroke-width="3"/></svg>秘密厳守</div>
      <div class="feature"><svg width="24" height="24" viewBox="0 0 24 24"><circle cx="12" cy="12" r="10" fill="none" stroke="#3fa535" stroke-width="3"/><path d="M12 6v6l4 3" fill="none" stroke="#3fa535" stroke-width="3"/></svg>即日作業</div>
      <div class="feature"><svg width="26" height="24" viewBox="0 0 26 24"><path d="M13 2L2 12h4v10h14V12h4z" fill="#3fa535"/></svg>家屋<br>補償付</div>
      <div class="feature"><svg width="24" height="24" viewBox="0 0 24 24"><path d="M4 13l6 6L21 5" fill="none" stroke="#3fa535" stroke-width="3.5"/></svg>追加料金<br>なし</div>
      <div class="feature"><svg width="24" height="24" viewBox="0 0 24 24"><path d="M12 21s-9-6-9-12a5 5 0 019-3 5 5 0 019 3c0 6-9 12-9 12z" fill="#3fa535"/></svg>女性<br>スタッフ</div>
    </div>
    <div class="budget">ご予算はご相談ください!お役に立たせてください!</div>
    <div class="flow">
      <div class="flow-label">ご依頼<br>の流れ</div>
      <div class="step">お問い合わせ</div><div class="arrow"></div>
      <div class="step">お伺い</div><div class="arrow"></div>
      <div class="step">お見積</div><div class="arrow"></div>
      <div class="step">作業</div><div class="arrow"></div>
      <div class="step">お支払</div>
    </div>
    <div class="contact">
      <p>ご相談・<strong>お見積無料!</strong><br>お気軽にお問い合わせください<br>そよかぜクリーンサービス</p>
      <div class="tel"><svg width="42" height="42" viewBox="0 0 24 24"><path d="M6.6 10.8a15 15 0 006.6 6.6l2.2-2.2a1 1 0 011-.25 11 11 0 003.6.6 1 1 0 011 1V20a1 1 0 01-1 1A17 17 0 013 4a1 1 0 011-1h3.5a1 1 0 011 1 11 11 0 00.6 3.6 1 1 0 01-.25 1z" fill="#23862a"/></svg><span>TEL.</span>000-000-000</div>
    </div>
  </section>
</main>
</body>
</html>
```